Marks of Dunmore business card design

I need a clean, professional looking design using the attached logo with a bright green/ gray/dark gray/black colors. Maybe even an orange accent if it looks good. I am open to slight changes in the logo if needed. Details below on the info on what should be on the cards. We are a sign company in Ft. Lauderdale FL that specializes in yacht lettering on multi million dollar yachts.

Target Market(s)

marine industry, yachts

Industry/Entity Type

Business

Colors
9bcb3c
000000
606060
f37122

Requirements
Must have
• address: 4837 W. Tallow Rd.
• Harbor Point, FL 33412
• Phone: 954-518-4062
• email/website: marksofdunmore@postvane.com MarksofDunmore.com
Nice to have
• I would like it very clean and simple but professional looking. Nice layout and would prefer a darker background. Orange highlight only if it works.
Should not have
• Nothing fancy.

```html
<!DOCTYPE html>
<html lang="en">
<head>
<meta charset="utf-8">
<title>Marks of Dunmore — Business Card</title>
<link href="https://fonts.googleapis.com/css2?family=Work+Sans:wght@400;500;700&display=swap" rel="stylesheet">
<style>
  :root {
    --page-bg: #e6e6e6;
    --card-bg: #1d1e1e;
    --brand-green: #0b9a3e;
    --accent-orange: #f37122;
    --text-light: #e9e9e9;
    --text-soft: #cfcfcf;
  }
  html, body {
    margin: 0;
    padding: 0;
    width: 1200px;
    height: 801px;
    overflow: hidden;
    background: var(--page-bg);
    font-family: "Work Sans", Arial, sans-serif;
  }
  .business-card {
    position: absolute;
    left: 150px;
    top: 143px;
    width: 900px;
    height: 514px;
    background: var(--card-bg);
    box-shadow: 0 10px 30px rgba(0,0,0,0.25);
    overflow: hidden;
  }
  .brand-name {
    position: absolute;
    top: 62px;
    right: 150px;
    margin: 0;
    font-size: 50px;
    font-weight: 700;
    letter-spacing: 0.5px;
    color: var(--brand-green);
    text-transform: uppercase;
    white-space: nowrap;
  }
  .contact-block {
    position: absolute;
    left: 90px;
    top: 252px;
    color: var(--text-light);
  }
  .person-name {
    margin: 0;
    font-size: 26px;
    font-weight: 400;
    letter-spacing: 2.5px;
    color: var(--brand-green);
    text-transform: uppercase;
  }
  .person-title {
    margin: 6px 0 0 8px;
    font-size: 15px;
    font-weight: 500;
    letter-spacing: 1px;
  }
  .address {
    margin: 24px 0 0 18px;
    font-style: normal;
    font-size: 15px;
    line-height: 21px;
    color: var(--text-soft);
  }
  .contact-list {
    list-style: none;
    margin: 14px 0 0 18px;
    padding: 0;
    font-size: 15px;
    line-height: 21px;
    color: var(--text-soft);
  }
  .contact-list li {
    display: flex;
    align-items: center;
    gap: 14px;
  }
  .contact-icon {
    width: 10px;
    height: 10px;
    fill: none;
    stroke: var(--brand-green);
    stroke-width: 1.6;
  }
  .accent-band {
    position: absolute;
    left: 0;
    bottom: 0;
    width: 100%;
    height: 18px;
    display: flex;
  }
  .accent-band .band-orange { flex: 0 0 45%; background: var(--accent-orange); }
  .accent-band .band-green { flex: 1; background: var(--brand-green); }
</style>
</head>
<body>
  <article class="business-card">
    <h1 class="brand-name">Marks of Dunmore</h1>

    <section class="contact-block">
      <h2 class="person-name">Dorian Vale</h2>
      <p class="person-title">CEO</p>
      <address class="address">
        4837 W. Tallow Rd.<br>
        Harbor Point, FL 33412
      </address>
      <ul class="contact-list">
        <li>
          <svg class="contact-icon" viewBox="0 0 10 10" aria-hidden="true">
            <path d="M2 1 L4 3 L3 4.5 Q4.5 6.5 5.5 7 L7 6 L9 8 L7.5 9.2 Q3.5 8.5 0.8 2.5 Z"/>
          </svg>
          954-518-4062
        </li>
        <li>
          <svg class="contact-icon" viewBox="0 0 10 10" aria-hidden="true">
            <rect x="1" y="2" width="8" height="6"/>
            <path d="M1 2 L5 5.5 L9 2"/>
          </svg>
          marksofdunmore@postvane.com
        </li>
        <li>
          <svg class="contact-icon" viewBox="0 0 10 10" aria-hidden="true">
            <circle cx="5" cy="5" r="4"/>
            <path d="M1 5 H9 M5 1 Q2.5 5 5 9 M5 1 Q7.5 5 5 9"/>
          </svg>
          www.MarksofDunmore.com
        </li>
      </ul>
    </section>

    <div class="accent-band">
      <span class="band-orange"></span>
      <span class="band-green"></span>
    </div>
  </article>
</body>
</html>
```